NEW Website DESIGN for Glass & Solid Surfaces Company

Brand New website, contemporary, clean, visual (images), not busy. ATTACHED IS OUR LOG THAT YOU MUST USE.

The company is called Brightwell Panes & Stoneworks (BrightwellPS)
www.brightwellps.com
The website should be www.brightwellpns.com
one page for glass one page for solid surfaces www.brightwellpanesplashes.co.uk
www.brightwellstoneworkss.co.uk

Target Market(s)

Hotels, Commercial projects, Small focus on residential

Industry/Entity Type

Construction

Number of Pages Required

5+ page

Font styles to use
Sans Serif

Requirements
Must have
• COLOURS AS PER OUR LOGO - WHITE/YELLOW/GREY - WHITE BACK GROUND
• CLEAR SIMPLE NAVIGATION - MODER CLEAN CUT - DESIGN FEEL
• LATEST NAVIGATION FOR IMAGES and text to include per project details
• WORK/PROJECT AREA - NEWS AREA - TEAM AREA/ABOUT US/CONTACT US
• NEW PAGEwww.brightwellpanesplashes.co.uk - NEW PAGE www.brightwellstoneworkss.co.uk
• PLEASE COPY THIS TYPE OF TEMPALTE
• https://www.harlowmead.co.uk/project/grand-halls/
• MOBILE READY
• WORDPRESS
• MODERN IMAGES INCLUDING VELMARA KESTRIN AND GLASS PROJECTS
Nice to have
• NEW DESIGN MODER FRESH
• WEBSITES I LIKE THE TEMPLATE SHOULD BE LIKE THE WEBSITE BELOW
• https://www.harlowmead.co.uk/
Should not have
• NOT Old fashion template, not busy NAVIGATION
• NO BLACK
• NO DARK GREYS
• NOT LOTS OF YELLOW
• RESDENTIAL IMAGES

```html
<!DOCTYPE html>
<html lang="en">
<head>
<meta charset="utf-8">
<title>Brightwell Panes & Stoneworks</title>
<link rel="stylesheet" href="https://fonts.googleapis.com/css2?family=Oswald:wght@400;500;600&family=Open+Sans:wght@400;600&display=swap">
<style>
:root{
  --yellow:#f2e21a;
  --grey:#8a8a8a;
  --grey-mid:#a9a9a9;
  --grey-light:#e9e9e9;
  --text:#555;
  --heading:#3a3a3a;
  --white:#fff;
  --hero-a:#d9dde0;--hero-b:#b9c0c4;
  --teal-a:#4fb7c2;--teal-b:#7fc6a8;
}
*{box-sizing:border-box;margin:0;padding:0}
html,body{width:1200px;height:2968px;overflow:hidden;background:var(--white);font-family:"Open Sans",Arial,sans-serif;color:var(--text)}
.page{position:relative;width:1200px;height:2968px}
.abs{position:absolute}
.photo{position:absolute}
h2,.heading{font-family:"Oswald",Arial,sans-serif;font-weight:600;color:var(--heading);text-transform:uppercase;letter-spacing:1px}
.btn{position:absolute;background:var(--grey);color:var(--white);font-family:"Oswald",Arial,sans-serif;font-size:13px;letter-spacing:1px;text-transform:uppercase;display:flex;align-items:center;justify-content:center;width:120px;height:30px}
.divider{position:absolute;left:584px;width:32px;height:32px;border-radius:50%;background:var(--white);border:2px solid var(--grey-light);display:flex;align-items:center;justify-content:center}
.divider::after{content:"";width:10px;height:10px;border-radius:50%;background:var(--grey-mid)}
/* hero */
.hero{left:0;top:0;width:1200px;height:640px;background:linear-gradient(120deg,var(--hero-a),#f3f4f4 45%,var(--hero-b))}
.brand{left:150px;top:26px;display:flex;align-items:center;gap:10px;font-family:"Oswald",Arial,sans-serif;font-size:15px;font-weight:500;color:var(--white);letter-spacing:1px}
.brand .mark{width:26px;height:26px;border-radius:50%;background:var(--yellow)}
.menu{left:1000px;top:40px}
.hero-title{left:150px;top:484px;font-family:"Oswald",Arial,sans-serif;font-weight:600;font-size:50px;color:var(--white);letter-spacing:2px}
.hero-sub{left:152px;top:556px;font-family:"Oswald",Arial,sans-serif;font-size:22px;color:var(--white);letter-spacing:1px}
.hero-sub b{color:var(--yellow);font-weight:500}
/* about */
.about-card{left:152px;top:730px;width:460px;height:236px;background:var(--white);box-shadow:0 4px 18px rgba(0,0,0,.12);padding:26px 30px}
.about-card h2{font-size:28px;margin-bottom:12px}
.about-card p{font-size:11px;line-height:19px;color:#777}
.about-photo{left:620px;top:716px;width:430px;height:250px;background:linear-gradient(135deg,#eef0f1,#c9ced1 60%,#f4f4f4)}
.corner{position:absolute;border-color:var(--yellow);border-style:solid}
/* projects */
.section-title{position:absolute;left:0;width:1200px;text-align:center;font-size:30px}
.project{top:1176px;height:264px}
.caption{position:absolute;left:14px;bottom:18px;color:var(--white);font-size:13px;font-family:"Oswald",Arial,sans-serif;letter-spacing:1px}
/* team */
.member{top:1636px;width:276px;height:264px;background:linear-gradient(180deg,#f1f1f1,#d6dade);box-shadow:0 4px 14px rgba(0,0,0,.1)}
.member-info{position:absolute;width:276px;text-align:center}
.member-info .name{font-family:"Oswald",Arial,sans-serif;font-size:18px;color:var(--heading);letter-spacing:1px}
.member-info .name.hl{color:#c9b900}
.member-info .line{font-size:12px;color:#777;margin-top:8px;display:flex;align-items:center;justify-content:center;gap:8px}
/* blog */
.blog-tile{position:absolute}
.tile-label{position:absolute;left:14px;top:14px;background:rgba(255,255,255,.85);padding:8px 12px;width:170px}
.tile-label b{display:block;font-family:"Oswald",Arial,sans-serif;font-weight:500;font-size:14px;color:var(--heading)}
.tile-label span{display:block;font-size:10px;line-height:15px;color:#777;margin-top:4px}
.blog-box{left:904px;top:2068px;width:296px;height:340px;background:var(--white);box-shadow:-4px 4px 18px rgba(0,0,0,.12);padding:26px 24px}
.blog-box h2{font-size:30px;line-height:36px;margin-bottom:14px}
.blog-box p{font-size:11px;line-height:19px;color:#777}
/* contact */
.contact-bg{left:0;top:2480px;width:1200px;height:440px;background:linear-gradient(100deg,var(--teal-a),#9fd3d6 45%,var(--teal-b) 70%,#e4e6e2)}
.contact-panel{left:720px;top:2480px;width:380px;height:420px;background:rgba(255,255,255,.78);padding:32px 36px}
.contact-panel h2{font-size:24px;text-align:center;margin-bottom:24px}
.field{height:38px;border-bottom:1px solid #bbb;font-size:12px;color:#888;display:flex;align-items:flex-end;padding-bottom:6px;margin-bottom:14px}
.field.msg{height:92px}
footer{position:absolute;left:0;top:2920px;width:1200px;height:48px;background:var(--white);border-top:1px solid var(--grey-light);display:flex;align-items:center;justify-content:space-between;padding:0 150px;font-size:11px;color:#888}
.socials{display:flex;gap:10px}
.socials i{width:14px;height:14px;border-radius:50%;background:var(--grey-mid);display:block}
</style>
</head>
<body>
<div class="page">

  <!-- Hero -->
  <div class="photo hero" role="img" aria-label="Bright white bedroom and living space with glass partition walls"></div>
  <div class="abs brand"><span class="mark"></span>Brightwell Panes &amp; Stoneworks</div>
  <svg class="abs menu" width="40" height="30" viewBox="0 0 40 30"><g stroke="#f2e21a" stroke-width="3"><line x1="2" y1="4" x2="38" y2="4"/><line x1="2" y1="15" x2="38" y2="15"/><line x1="2" y1="26" x2="38" y2="26"/></g></svg>
  <div class="abs hero-title">BRIGHTWELL SPLASHBACKS</div>
  <div class="abs hero-sub">VELMARA, GLASS, MIRROR... COMPLETELY <b>BESPOKE</b></div>
  <div class="divider" style="top:648px"></div>

  <!-- About -->
  <div class="photo about-photo" role="img" aria-label="Modern bathroom with solid surface vanity and glass splashback"></div>
  <div class="corner" style="left:1000px;top:702px;width:64px;height:64px;border-width:4px 4px 0 0"></div>
  <div class="abs about-card">
    <h2>About Us</h2>
    <p>We design, make and fit bespoke glass splashbacks, mirrors and solid surface worktops for hotels, offices and commercial spaces across the region. Every piece is measured on site, cut to fit and finished by our own skilled fitters. From a single panel to a full hotel refit, we deliver clean lines, strong finishes and work that lasts for years to come.</p>
  </div>
  <div class="btn" style="left:540px;top:952px">Read More</div>

  <div class="divider" style="top:1044px"></div>

  <!-- Projects -->
  <h2 class="section-title" style="top:1104px">Our Recent Projects</h2>
  <div class="photo project" style="left:0;width:140px;background:linear-gradient(160deg,#3c4a55,#8a9aa5)" role="img" aria-label="Dark tiled shower with glass screen"></div>
  <div class="photo project" style="left:160px;width:284px;background:linear-gradient(160deg,#c7b89a,#e8dcc4)" role="img" aria-label="Bathroom with bath and glass panels"></div>
  <div class="photo project" style="left:460px;width:284px;background:linear-gradient(160deg,#d4d8dc,#a7afb6)" role="img" aria-label="Glass splashback kitchen project">
    <div class="caption">Velmara &amp; glass kitchen refit</div>
  </div>
  <div class="photo project" style="left:760px;width:284px;background:linear-gradient(160deg,#eef0f2,#9aa3ab)" role="img" aria-label="White kitchen with solid surface worktops"></div>
  <div class="photo project" style="left:1056px;width:144px;background:linear-gradient(160deg,#f2ede4,#c7b79c)" role="img" aria-label="Bright hallway with glass doors"></div>
  <div class="corner" style="left:1050px;top:1150px;width:64px;height:64px;border-width:4px 0 0 4px"></div>
  <div class="btn" style="left:540px;top:1488px">View More</div>

  <!-- Team -->
  <h2 class="section-title" style="top:1564px">Our Awesome Team</h2>
  <div class="photo member" style="left:160px" role="img" aria-label="Team member portrait in safety helmet"></div>
  <div class="photo member" style="left:462px" role="img" aria-label="Team member portrait in work cap"></div>
  <div class="photo member" style="left:764px" role="img" aria-label="Team member portrait in hard hat"></div>
  <svg class="abs" style="left:660px;top:1836px" width="78" height="64" viewBox="0 0 78 64"><polygon points="78,0 78,64 0,64" fill="#f2e21a"/></svg>
  <div class="member-info" style="left:160px;top:1916px"><div class="name">ELLA MARSH</div><div class="line">+1 (717) 555-0142</div><div class="line">ella@brightwellps.com</div></div>
  <div class="member-info" style="left:462px;top:1916px"><div class="name hl">TOBIAS RENNER</div><div class="line">+1 (717) 555-0167</div><div class="line">tobias@brightwellps.com</div></div>
  <div class="member-info" style="left:764px;top:1916px"><div class="name">JON DALE</div><div class="line">+1 (717) 555-0189</div><div class="line">jon@brightwellps.com</div></div>

  <!-- Blog -->
  <div class="blog-tile" style="left:0;top:2080px;width:420px;height:320px;background:linear-gradient(140deg,#e7d6cc,#c79c8c)" role="img" aria-label="Glass partitioned washroom interior">
    <div class="tile-label" style="top:160px"><b>Glass Partitions</b><span>How frameless glass opens up a small hotel room.</span></div>
  </div>
  <div class="blog-tile" style="left:400px;top:2080px;width:230px;height:320px;background:linear-gradient(160deg,#f1f2f4,#d17fc0)" role="img" aria-label="Hotel lounge with pink glass panels">
    <div class="tile-label"><b>Hotel Lounges</b><span>Colour glass for bars and reception desks.</span></div>
  </div>
  <div class="blog-tile" style="left:630px;top:2080px;width:274px;height:320px;background:linear-gradient(160deg,#d9dcdf,#8d959c)" role="img" aria-label="Kitchen with grey glass splashback">
    <div class="tile-label" style="top:140px"><b>Splashbacks</b><span>Choosing the right tone for your kitchen.</span></div>
  </div>
  <div class="abs blog-box">
    <h2>Latest News<br>From Our Blog</h2>
    <p>Read our latest project stories, fitting tips and new material guides. We share what we learn on every hotel, office and shop fit, so you can plan your own space with ease and pick the right finish first time.</p>
  </div>
  <div class="btn" style="left:984px;top:2370px">Read More</div>

  <div class="divider" style="top:2458px"></div>

  <!-- Contact -->
  <div class="photo contact-bg" role="img" aria-label="Lift lobby with teal and green glass wall panels and a potted plant"></div>
  <div class="abs contact-panel">
    <h2>Contact Us Today!</h2>
    <div class="field">Your Name</div>
    <div class="field">Email Address</div>
    <div class="field">Phone Number</div>
    <div class="field msg">Your Message</div>
  </div>
  <div class="btn" style="left:850px;top:2840px">Submit</div>

  <footer>
    <span>© Brightwell Panes &amp; Stoneworks. All rights reserved.</span>
    <div class="socials"><i></i><i></i><i></i></div>
  </footer>
</div>
</body>
</html>
```